WWW.VELTRONA.IT BUSINNES CARD

WE NEED A BUSINESS CARD . I HAVE A COMPANY IN ITALY NR 1 IN HAIR MEDICAL CARE AN HAIR REPLECEMENT . IN CARD I NEED WRITE WEB ADDRESS, MAIL , ADDRESS, TELEPHONE NUMBER , AND NAME
IN THE BACK SIDE I NEED MY DOCTOR LOGO .
MY WEB SITE IS WWW.VELTRONA.IT
Updates

Target Market(s)

CONSUMER B2C

Industry/Entity Type

Hair And Beauty

Contact Information for Business Card

I WANT A MEDICAL BUSINESS CARD.

Font styles to use
Other font styles liked:
• VERDANA

Colors
33a6d7
3176b5
85abd2
aedbee
eaf1f7
ffffff

Requirements
Must have
• I NEED MY LOGO AND LOGO OF DR VELTRONA

```html
<!DOCTYPE html>
<html lang="it">
<head>
<meta charset="utf-8">
<title>Veltrona – Biglietto da visita</title>
<link rel="stylesheet" href="https://fonts.googleapis.com/css2?family=Noto+Sans:ital,wght@0,400;0,700;1,700&display=swap">
<style>
  :root{
    --page:#ececec;
    --white:#ffffff;
    --navy:#0f4d94;
    --brand-blue:#3176b5;
    --sky:#33a6d7;
    --soft:#85abd2;
    --pale:#aedbee;
    --mist:#eaf1f7;
    --ink:#3d3d3d;
    --label:#4a4a4a;
  }
  *{margin:0;padding:0;box-sizing:border-box}
  html,body{width:1200px;height:1200px;overflow:hidden;background:var(--page)}
  body{font-family:"Noto Sans",Verdana,sans-serif;position:relative}
  .card{position:absolute;left:217px;width:766px;height:438px;background:var(--white);overflow:hidden}
  .card--front{top:92px}
  .card--back{top:611px}
  .card__art{position:absolute;inset:0;width:100%;height:100%}

  .brand{position:absolute;left:0;right:0;top:118px;display:flex;justify-content:center;align-items:center;gap:14px}
  .brand__dot{width:30px;height:30px;border-radius:50%;background:var(--sky)}
  .brand__name{font-weight:700;font-size:66px;line-height:1;color:var(--navy);letter-spacing:0.5px}
  .tagline{position:absolute;left:0;right:0;top:220px;text-align:center;font-size:20px;color:var(--navy);letter-spacing:0.6px}

  .contact{position:absolute;display:flex;align-items:flex-start;gap:10px;font-size:14px;color:var(--ink);line-height:16px;white-space:nowrap}
  .contact svg{flex:none;width:18px;height:18px;fill:var(--brand-blue);margin-top:-2px}
  .contact__city{color:var(--label);font-weight:700;text-decoration:underline;text-underline-offset:3px;margin-right:4px}
  .contact__lines{display:inline-block;vertical-align:top}
  .contact__indent{padding-left:62px;display:block}

  .doctor-figure{position:absolute;left:651px;top:233px;width:64px;height:200px;border-radius:32px 32px 8px 8px;background:linear-gradient(180deg,#8a5a3c,#6b4a38 60%,#dfe9f5)}
  .doctor-label{position:absolute;left:510px;top:402px;font-size:21px;font-weight:700;color:#1b4f9a}
</style>
</head>
<body>

<section class="card card--front" aria-label="Fronte del biglietto">
  <svg class="card__art" viewBox="0 0 957 547" preserveAspectRatio="none" aria-hidden="true">
    <defs>
      <linearGradient id="blueBand" x1="0" y1="0" x2="1" y2="0">
        <stop offset="0" stop-color="#85bdf8"/><stop offset="1" stop-color="#3f86d6"/>
      </linearGradient>
      <linearGradient id="paleBand" x1="0" y1="0" x2="1" y2="0">
        <stop offset="0" stop-color="#aedbee"/><stop offset="1" stop-color="#e6f6fd"/>
      </linearGradient>
      <linearGradient id="fade" x1="0" y1="1" x2="1" y2="0">
        <stop offset="0" stop-color="#eaf1f7" stop-opacity="0"/><stop offset="1" stop-color="#d6effb"/>
      </linearGradient>
    </defs>
    <path d="M270 0 H370 L300 70 Q282 88 255 88 H200 Z" fill="url(#paleBand)"/>
    <path d="M0 0 H272 L125 160 Q104 183 75 183 H0 Z" fill="url(#blueBand)"/>
    <path d="M0 183 H75 Q104 183 125 160 L135 150 Q115 212 75 212 H0 Z" fill="#f3f6fa"/>
    <path d="M870 0 H957 V120 L840 240 H740 Z" fill="url(#fade)"/>
    <path d="M0 500 L120 380 H260 L90 547 H0 Z" fill="url(#fade)" opacity="0.6"/>
    <path d="M60 547 L190 420 H320 L180 547 Z" fill="#e3f4fc" opacity="0.7"/>
    <path d="M150 547 L165 530 Q180 510 210 510 H700 L690 547 Z" fill="#f2f5f9"/>
    <path d="M505 510 L600 430 Q625 410 650 410 H700 L580 510 Z" fill="url(#paleBand)"/>
    <path d="M605 510 L720 395 Q735 382 760 382 H850 L740 495 Q725 510 700 510 Z" fill="url(#blueBand)"/>
    <path d="M775 547 L870 450 Q890 435 910 435 H957 V547 Z" fill="url(#paleBand)"/>
    <path d="M830 547 L957 420 V547 Z" fill="url(#blueBand)"/>
    <path d="M184 360 C330 320 450 370 560 378 C660 385 740 360 777 325" fill="none" stroke="#29b0e3" stroke-width="4" stroke-linecap="round"/>
  </svg>
  <div class="brand">
    <span class="brand__dot"></span>
    <span class="brand__name">Veltrona</span>
  </div>
  <p class="tagline">CURA E REINTEGRAZIONE DEI CAPELLI</p>
</section>

<section class="card card--back" aria-label="Retro del biglietto">
  <svg class="card__art" viewBox="0 0 957 547" preserveAspectRatio="none" aria-hidden="true">
    <defs>
      <linearGradient id="blueBand2" x1="0" y1="0" x2="1" y2="0">
        <stop offset="0" stop-color="#85bdf8"/><stop offset="1" stop-color="#3f86d6"/>
      </linearGradient>
      <linearGradient id="paleBand2" x1="0" y1="0" x2="1" y2="0">
        <stop offset="0" stop-color="#aedbee"/><stop offset="1" stop-color="#e6f6fd"/>
      </linearGradient>
      <linearGradient id="fade2" x1="0" y1="1" x2="1" y2="0">
        <stop offset="0" stop-color="#eaf1f7" stop-opacity="0"/><stop offset="1" stop-color="#d6effb"/>
      </linearGradient>
    </defs>
    <path d="M330 0 H420 L380 20 Q360 28 330 28 Z" fill="url(#paleBand2)"/>
    <path d="M0 0 H330 L285 45 Q268 60 240 60 H0 Z" fill="url(#blueBand2)"/>
    <path d="M0 60 H240 Q268 60 285 45 L300 30 Q275 90 230 90 H0 Z" fill="#f3f6fa"/>
    <path d="M900 0 H957 V100 L820 230 H740 Z" fill="url(#fade2)"/>
    <path d="M0 500 L90 420 H200 L60 547 H0 Z" fill="url(#fade2)" opacity="0.6"/>
    <path d="M40 547 L170 430 H270 L150 547 Z" fill="#e6f5fc" opacity="0.8"/>
    <path d="M700 290 Q720 262 760 262 H957 V290 Z" fill="#f3f6fa"/>
    <path d="M435 547 L625 340 Q645 325 670 325 H740 L530 547 Z" fill="url(#paleBand2)"/>
    <path d="M530 547 L740 310 Q760 290 790 290 H957 V547 Z" fill="url(#blueBand2)"/>
  </svg>

  <div class="contact" style="left:94px;top:90px">
    <svg viewBox="0 0 24 24"><path d="M12 2a7 7 0 0 0-7 7c0 5 7 13 7 13s7-8 7-13a7 7 0 0 0-7-7zm0 9.5A2.5 2.5 0 1 1 12 6.5a2.5 2.5 0 0 1 0 5z"/></svg>
    <span><span class="contact__city">Firenze</span>Via dei Ciliegi, 42/3</span>
  </div>
  <div class="contact" style="left:379px;top:90px">
    <svg viewBox="0 0 24 24"><path d="M12 2a7 7 0 0 0-7 7c0 5 7 13 7 13s7-8 7-13a7 7 0 0 0-7-7zm0 9.5A2.5 2.5 0 1 1 12 6.5a2.5 2.5 0 0 1 0 5z"/></svg>
    <span><span class="contact__city">Vicenza</span>Via dell’Artigiano 27</span>
  </div>
  <div class="contact" style="left:94px;top:134px">
    <svg viewBox="0 0 24 24"><path d="M12 2a7 7 0 0 0-7 7c0 5 7 13 7 13s7-8 7-13a7 7 0 0 0-7-7zm0 9.5A2.5 2.5 0 1 1 12 6.5a2.5 2.5 0 0 1 0 5z"/></svg>
    <span><span class="contact__city">Livorno</span>Via delle Rondini, 117</span>
  </div>
  <div class="contact" style="left:379px;top:134px">
    <svg viewBox="0 0 24 24"><path d="M12 2a7 7 0 0 0-7 7c0 5 7 13 7 13s7-8 7-13a7 7 0 0 0-7-7zm0 9.5A2.5 2.5 0 1 1 12 6.5a2.5 2.5 0 0 1 0 5z"/></svg>
    <span><span class="contact__city">Verona</span>Via Leopardi, 31</span>
  </div>
  <div class="contact" style="left:94px;top:178px">
    <svg viewBox="0 0 24 24"><path d="M12 2a7 7 0 0 0-7 7c0 5 7 13 7 13s7-8 7-13a7 7 0 0 0-7-7zm0 9.5A2.5 2.5 0 1 1 12 6.5a2.5 2.5 0 0 1 0 5z"/></svg>
    <span class="contact__lines"><span class="contact__city">Modena</span>Presso Centro Ninfea Loc. Borgo Alto<span class="contact__indent">Via Giuseppe Montanari Ferretti, 6/b</span></span>
  </div>
  <div class="contact" style="left:94px;top:226px">
    <svg viewBox="0 0 24 24"><path d="M12 2a7 7 0 0 0-7 7c0 5 7 13 7 13s7-8 7-13a7 7 0 0 0-7-7zm0 9.5A2.5 2.5 0 1 1 12 6.5a2.5 2.5 0 0 1 0 5z"/></svg>
    <span><span class="contact__city">Treviso</span> Via Sansovino 58</span>
  </div>
  <div class="contact" style="left:94px;top:272px">
    <svg viewBox="0 0 24 24"><path d="M2 9l10-6 10 6v11H2z M4 10.2l8 5 8-5"/></svg>
    <span>info@veltrona.it</span>
  </div>
  <div class="contact" style="left:94px;top:317px">
    <svg viewBox="0 0 24 24"><path d="M6.6 10.8a15 15 0 0 0 6.6 6.6l2.2-2.2a1 1 0 0 1 1-.25 11.4 11.4 0 0 0 3.6.6 1 1 0 0 1 1 1V20a1 1 0 0 1-1 1A17 17 0 0 1 3 4a1 1 0 0 1 1-1h3.5a1 1 0 0 1 1 1c0 1.25.2 2.45.6 3.6a1 1 0 0 1-.25 1z"/></svg>
    <span>800 517390</span>
  </div>
  <div class="contact" style="left:94px;top:363px">
    <svg viewBox="0 0 24 24"><path d="M6 2l13 11-6 .6 3.5 7-2.6 1.2-3.4-7L6 19z"/></svg>
    <span>www.veltrona.it</span>
  </div>

  <div class="doctor-figure" role="img" aria-label="Mascotte del dottore Veltrona: personaggio a forma di capello in camice bianco"></div>
  <p class="doctor-label">dr. Veltrona</p>
</section>

</body>
</html>
```